Divorce marketing brochure - Which will include a toy ball and chain as a gimick

A single page marketing enclosure which includes a toy ball and chain to be given to lawyers. I want to convey the following messages:

1. We pay a 1/3 referral fee;
2. We solve difficult problems.

Examples of problems solved:
*Litigation of complex property, custody, support and parenting time issues;
*Protection (or invasion) of personal injury proceeds in divorce;
*Distribution of consortium proceeds in divorce;
*Pre-nuptial and Post-nuptial agreements.
*Settlements
*Reduce conflict

A sample of the toy ball and chain enclosure can be viewed here:

My website is www.thesplitcounsel.com (currently being updated - who's isn't?)

http://www.shopvexto.com/Orbel-Trinkets-Inc-Convict-Shackle/dp/K7QX3MZP21/ref=sr_1_9?ie=UTF8&qid=1311011554&sr=8-9

Target Market(s)

Personal Injury Attorneys

Industry/Entity Type

Marketing

Requirements
Must have
• Call to action:

www.thesplitcounsel.com
1-877-HIRE-TEAM
248-555-7182
Marcus@brevanlegal.com
Nice to have
• I want this campaign to stand out. Different is good. I am a divorce lawyer marketing to personal injury attorneys (and some others) for divorce referrals. (No one forgets the girl with red hair and braces) I want the campaign to be remembered without being offensive.
Should not have

```html
<!DOCTYPE html>
<html lang="en">
<head>
<meta charset="utf-8">
<title>Brevan Family Law – Referral Enclosure</title>
<link href="https://fonts.googleapis.com/css2?family=Open+Sans:wght@400;700&family=Oswald:wght@600&display=swap" rel="stylesheet">
<style>
  :root {
    --ink-dark: #050808;
    --steel-deep: #1d2a2c;
    --steel-mid: #55686a;
    --steel-light: #c9d6d2;
    --brand-text: #e6e9e8;
    --list-text: #e6e9e8;
    --white: #ffffff;
    --band-green: #22e000;
    --band-shadow: #9a9a9a;
    --footer-text: #111111;
  }
  html, body {
    margin: 0;
    padding: 0;
    overflow: hidden;
    background: var(--white);
  }
  .enclosure {
    position: relative;
    width: 1200px;
    height: 743px;
    overflow: hidden;
    background: var(--white);
  }
  .hero-photo {
    position: absolute;
    inset: 0 0 auto 0;
    height: 660px;
    background:
      radial-gradient(ellipse 230px 230px at 1010px 390px, var(--steel-light) 0%, #8a9b98 35%, var(--steel-mid) 60%, rgba(29,42,44,0) 100%),
      radial-gradient(ellipse 520px 360px at 880px 180px, rgba(110,130,128,0.55) 0%, rgba(29,42,44,0) 100%),
      linear-gradient(180deg, var(--ink-dark) 0%, var(--steel-deep) 55%, #2a3a3b 100%);
  }
  .brand-name {
    position: absolute;
    left: 44px;
    top: 48px;
    margin: 0;
    font-family: "Oswald", sans-serif;
    font-weight: 600;
    font-size: 74px;
    line-height: 1;
    color: var(--brand-text);
  }
  .problems-title {
    position: absolute;
    left: 48px;
    top: 168px;
    margin: 0;
    font-family: "Oswald", sans-serif;
    font-weight: 600;
    font-size: 40px;
    letter-spacing: 0.6px;
    line-height: 1.2;
    color: var(--white);
  }
  .problems-list {
    position: absolute;
    left: 48px;
    top: 254px;
    margin: 0;
    padding: 0;
    list-style: none;
    font-family: "Open Sans", sans-serif;
    font-weight: 400;
    font-size: 22px;
    line-height: 30px;
    color: var(--list-text);
  }
  .problems-list li { white-space: pre; }
  .offer-band {
    position: absolute;
    left: 0;
    top: 530px;
    width: 1200px;
    height: 170px;
  }
  .offer-lines {
    position: absolute;
    left: 20px;
    top: 564px;
    margin: 0;
    font-family: "Oswald", sans-serif;
    font-weight: 600;
    font-size: 31px;
    line-height: 50px;
    color: var(--white);
  }
  .offer-lines span { display: block; }
  .contact-bar {
    position: absolute;
    left: 0;
    top: 700px;
    width: 1200px;
    height: 43px;
    font-family: "Open Sans", sans-serif;
    font-weight: 700;
    font-size: 16px;
    color: var(--footer-text);
  }
  .contact-item {
    position: absolute;
    top: 5px;
  }
  .contact-call { left: 65px; }
  .contact-mail { left: 432px; }
  .contact-web { left: 806px; }
</style>
</head>
<body>
  <main class="enclosure">
    <div class="hero-photo" role="img" aria-label="Photograph of a steel ball and chain on a dark surface"></div>

    <h1 class="brand-name">Brevan Family Law</h1>

    <h2 class="problems-title">Examples of problems solved:</h2>
    <ul class="problems-list">
      <li>*Litigation of complex property, custody,</li>
      <li> support  and parenting time issues;</li>
      <li>*Protection (or invasion) of personal injury</li>
      <li>  proceeds in divorce;</li>
      <li>*Distribution of consortium proceeds in divorce;</li>
      <li>*Pre-nuptial and Post-nuptial agreements.</li>
      <li>*Settlements</li>
      <li>*Reduce conflict</li>
    </ul>

    <svg class="offer-band" viewBox="0 530 1200 170" aria-hidden="true">
      <path d="M0 545 C400 548 850 556 1200 568 L1200 650 C900 668 500 684 0 692 Z" fill="var(--band-shadow)" opacity="0.6"/>
      <path d="M0 543 C400 546 850 554 1200 564 L1200 636 C900 656 500 674 0 682 Z" fill="var(--band-green)"/>
    </svg>

    <p class="offer-lines">
      <span>We pay a 1/3 referral fee;</span>
      <span>We solve difficult problems.</span>
    </p>

    <footer class="contact-bar">
      <span class="contact-item contact-call">CALL ME: 248-555-7182</span>
      <span class="contact-item contact-mail">MAIL ME: Marcus@brevanlegal.com</span>
      <span class="contact-item contact-web">KNOW ME: www.thesplitcounsel.com</span>
    </footer>
  </main>
</body>
</html>
```